Apartment Brochure for Corvella Heights, Rockingham

We need a brochure prepared for a new apartment development in Rockingham.

We only require the template and first front pages and our in house designer can add the other pages and text as required.

Please provide brochure in Photoshop format with editable texts, and PDF format.

Brochure in A4 printable format.

Some of the text for brochure and all the illustrations can be found on the attached Powerpoint presentation.

The different sections of the brochure would be something like this:
1. The Development –
a. key information about the project (2 bedroom, priced from $355,000, quality finishings etc)
b. info on the amenities nearby (City park next door, shops across the road, beach down the road)
2. Why Invest in Rockingham - info on Rockingham
a. fast growing area of Western Australia
b. tourist hotspot
c. huge resource investment
d. good job opportunities
3. Development Plan & Floor Plan
4. About the Developer – Info about Beltor.

Feel free to contact me on 0417 586 921 or mervyn@beltor-example.com.au if you have any questions or require any further information. There is also the opportunity for more ongoing work!

Thank you!
Updates

Hello Everyone,

One page sample is fine at this stage. Please include Beltor logo, picture of apartments and the lake in the front of the brochure.

Photoshop version is preferred if you are successful in getting the job.

```html
<!DOCTYPE html>
<html lang="en">
<head>
<meta charset="utf-8">
<title>Corvella Heights — Brochure Cover</title>
<link href="https://fonts.googleapis.com/css2?family=Montserrat:wght@400;600&display=swap" rel="stylesheet">
<style>
  :root {
    --ink: #0b0b0b;
    --gold: #c9a24a;
    --edge: #e9dcb8;
    --white: #ffffff;
    --sky: #9fc2e4;
    --sky-pale: #dfe9f2;
    --building: #ecebe6;
    --roof: #4a4b4f;
    --hedge: #4e6b35;
    --road: #3a3b3e;
    --water: #3e7fa8;
    --water-deep: #2a5f86;
    --tree: #3c5a2a;
    --grass: #6a843f;
  }
  * { margin: 0; padding: 0; box-sizing: border-box; }
  html, body { width: 849px; height: 1200px; overflow: hidden; background: var(--white); }
  .cover {
    position: relative;
    width: 849px;
    height: 1200px;
    overflow: hidden;
    background: var(--ink);
    font-family: "Montserrat", sans-serif;
  }
  .photo { position: absolute; inset: 0; }
  .photo--apartments {
    background:
      linear-gradient(180deg, transparent 0%, transparent 58%, var(--road) 62%, #2e2f32 100%),
      linear-gradient(180deg, transparent 0%, transparent 50%, var(--hedge) 53%, #6d7f4c 57%, transparent 58%),
      linear-gradient(90deg, transparent 0%, transparent 8%, var(--building) 14%, #cfcdc7 40%, var(--building) 55%, #f4f3ef 80%, #d6d4ce 92%),
      linear-gradient(180deg, var(--sky) 0%, var(--sky-pale) 20%);
    background-size: 100% 100%, 100% 100%, 100% 45%, 100% 100%;
    background-position: 0 0, 0 0, 0 110px, 0 0;
    background-repeat: no-repeat;
    clip-path: polygon(0 0, 849px 0, 849px 113px, 424px 693px, 0 198px);
  }
  .photo--fountain-lake {
    background: linear-gradient(180deg, #5d93cc 0%, #a8c9e6 40%, #5c7d3f 58%, var(--tree) 68%, #7c8f58 74%, var(--water) 78%, #7fb0cf 84%, var(--water) 88%, var(--water-deep) 100%);
    clip-path: polygon(0 523px, 314px 905px, 314px 1200px, 0 1200px);
  }
  .photo--lakeside-lawn {
    background: linear-gradient(180deg, #a7c6e4 0%, #dbe7f0 22%, #4d6b3a 36%, var(--water) 42%, #8db4cc 52%, var(--water-deep) 58%, #93a56c 64%, var(--grass) 78%, #5c7634 100%);
    clip-path: polygon(849px 510px, 532px 905px, 532px 1200px, 849px 1200px);
  }
  .y-frame { position: absolute; inset: 0; }
  .y-frame__edge { fill: none; stroke: var(--edge); stroke-width: 2; }
  .brand {
    position: absolute;
    left: 314px;
    width: 218px;
    top: 826px;
    text-align: center;
  }
  .brand__name {
    display: block;
    color: var(--gold);
    font-weight: 600;
    font-size: 32px;
    line-height: 36px;
    letter-spacing: 3px;
  }
  .brand__tagline {
    color: var(--white);
    font-weight: 400;
    font-size: 13px;
    letter-spacing: 0.5px;
    line-height: 24px;
    margin-top: 4px;
  }
</style>
</head>
<body>
  <main class="cover">
    <div class="photo photo--apartments" role="img" aria-label="Photo of the Corvella Heights apartment buildings with gardens and a road in front"></div>
    <div class="photo photo--fountain-lake" role="img" aria-label="Photo of a park lake with a fountain and trees"></div>
    <div class="photo photo--lakeside-lawn" role="img" aria-label="Photo of a lakeside lawn with water birds and a fountain"></div>

    <svg class="y-frame" width="849" height="1200" viewBox="0 0 849 1200" aria-hidden="true">
      <polygon fill="var(--ink)" points="0,198 424,693 849,113 849,510 532,905 532,1200 314,1200 314,905 0,523"/>
      <polyline class="y-frame__edge" points="0,198 424,693 849,113"/>
      <polyline class="y-frame__edge" points="0,523 314,905 314,1200"/>
      <polyline class="y-frame__edge" points="849,510 532,905 532,1200"/>
    </svg>

    <div class="brand">
      <span class="brand__name">BELTOR</span>
      <p class="brand__tagline">CREATING VALUE<br>SHARING VALUE</p>
    </div>
  </main>
</body>
</html>
```